A gang member and street hustler turned preacher needs a cover

A man who used to be a gang member and street hustler turned his life around and became a preacher. He has written a book titled Unsteepled: My Passage From Ashes to Glory and he needs a cover for the book. The book is a memoir about his life and his journey from the streets to the church. It details the lessons that he's learned along the way. I have attached a photo to incorporate in the cover design. <br/>Title: Unsteepled: My Passage From Ashes to Glory<br/>Author: Dr. Malcolm T. Hayward

```html
<!DOCTYPE html>
<html lang="en">
<head>
<meta charset="UTF-8">
<title>Unsteepled: My Passage From Ashes to Glory</title>
<link rel="stylesheet" href="https://fonts.googleapis.com/css2?family=Montserrat:ital,wght@0,300;0,700;0,800;0,900;1,300;1,400&display=swap">
<style>
  :root {
    --ink-deep: #151515;
    --ink-mid: #2c2d2c;
    --stone-light: #c9ccc4;
    --stone-mid: #6f716c;
    --title-red: #d0202a;
    --paper-white: #f4f4f1;
    --glow: #e9f6ff;
  }
  html, body {
    margin: 0;
    padding: 0;
    width: 800px;
    height: 1200px;
    overflow: hidden;
    background: var(--ink-deep);
  }
  .cover {
    position: relative;
    width: 800px;
    height: 1200px;
    overflow: hidden;
    background: linear-gradient(180deg, var(--ink-mid) 0%, #222322 55%, var(--ink-deep) 100%);
    font-family: "Montserrat", sans-serif;
  }
  .author-portrait {
    position: absolute;
    left: 0;
    top: 0;
    width: 800px;
    height: 720px;
    background:
      radial-gradient(ellipse 230px 300px at 480px 300px, #4a4b48 0%, rgba(40,41,40,0.9) 60%, rgba(30,30,30,0) 100%),
      linear-gradient(90deg, #3b3c3a 0%, #1d1e1d 30%, #2a2b29 70%, var(--stone-light) 100%);
    -webkit-mask-image: linear-gradient(180deg, #000 70%, transparent 100%);
            mask-image: linear-gradient(180deg, #000 70%, transparent 100%);
  }
  .cuffs-illustration {
    position: absolute;
    left: 280px;
    top: 640px;
    width: 520px;
    height: 420px;
    background:
      radial-gradient(circle 110px at 170px 200px, var(--glow) 0%, #9fb9c8 35%, rgba(80,80,78,0.9) 60%, rgba(60,60,58,0) 100%),
      radial-gradient(ellipse 260px 200px at 240px 220px, #6b6a66 0%, rgba(50,50,48,0.6) 60%, rgba(30,30,30,0) 100%);
  }
  .title-vertical {
    position: absolute;
    left: 90px;
    top: 60px;
    width: 130px;
    height: 980px;
  }
  .title-vertical text {
    fill: var(--title-red);
    font-family: "Montserrat", sans-serif;
    font-weight: 900;
    font-size: 140px;
  }
  .subtitle {
    position: absolute;
    left: 220px;
    width: 560px;
    top: 520px;
    text-align: center;
    color: var(--paper-white);
  }
  .subtitle-lead {
    font-style: italic;
    font-weight: 300;
    font-size: 32px;
    letter-spacing: 2px;
    margin: 0;
  }
  .subtitle-main {
    margin: 8px 0 0;
    font-size: 48px;
    font-weight: 800;
    letter-spacing: 1px;
  }
  .subtitle-main .accent { color: var(--title-red); }
  .subtitle-main .joiner {
    font-style: italic;
    font-weight: 300;
    font-size: 32px;
    margin: 0 6px;
  }
  .author-name {
    position: absolute;
    left: 0;
    width: 800px;
    top: 1090px;
    text-align: center;
    color: var(--paper-white);
    font-weight: 800;
    font-size: 38px;
    letter-spacing: 7px;
    margin: 0;
  }
</style>
</head>
<body>
  <main class="cover">
    <div class="author-portrait" role="img" aria-label="Black and white portrait of the author in a dark suit, smiling"></div>
    <div class="cuffs-illustration" role="img" aria-label="Open steel handcuffs with a glowing white cross shining through the cuff"></div>

    <svg class="title-vertical" viewBox="0 0 130 980" aria-label="Unsteepled">
      <text x="-980" y="118" transform="rotate(-90)" textLength="975" lengthAdjust="spacingAndGlyphs">UNSTEEPLED</text>
    </svg>

    <div class="subtitle">
      <p class="subtitle-lead">My Passage from</p>
      <p class="subtitle-main"><span class="accent">ASHES</span><span class="joiner">to</span>GLORY</p>
    </div>

    <p class="author-name">DR. MALCOLM T. HAYWARD</p>
  </main>
</body>
</html>
```